Garden of Eden - Digital Party Invite

I'm throwing a Halloween party with the theme "Garden of Eden". The invite will be sent via Tidewell Cards. I need a custom design for the invite. Here are the details:
The image needs to be 670x970.
Needs to be sexy - maybe with Adam & Eve, and the snake w/the apple, etc
Text should be:
You Are Invited To
The Garden of Eden
Sat Oct 26 7:00PM
at
Dinah & Tobias's Home
612 North Birch Rd 7B
Costumes Highly Encouraged
Adults Only Please

```html
<!DOCTYPE html>
<html lang="en">
<head>
<meta charset="UTF-8">
<title>The Garden of Eden – Halloween Party Invite</title>
<link href="https://fonts.googleapis.com/css2?family=Playfair+Display:wght@500;600&family=Montserrat:wght@400;500;600&display=swap" rel="stylesheet">
<style>
  :root {
    --stage: #ececec;
    --night: #0a0608;
    --moon-core: #f7e8ed;
    --moon-mid: #e9b9c7;
    --moon-rim: #c43460;
    --glow: #5c0d24;
    --hill: #050304;
    --crimson: #d61f57;
    --ink-dark: #2a0c16;
    --ink-light: #f3eef0;
    --line-light: rgba(243, 238, 240, 0.85);
  }
  * { margin: 0; padding: 0; box-sizing: border-box; }
  html, body {
    width: 1200px;
    height: 2172px;
    overflow: hidden;
    background: var(--stage);
  }
  .invite {
    position: absolute;
    left: 50px;
    top: 290px;
    width: 1100px;
    height: 1593px; /* 670 x 970 proportion */
    background: var(--night);
    color: var(--ink-light);
    font-family: "Montserrat", Arial, sans-serif;
    text-align: center;
    overflow: hidden;
  }
  .moonlit-scene {
    position: absolute;
    left: 0;
    top: 0;
    width: 1100px;
    height: 1100px;
    background:
      linear-gradient(to bottom, rgba(5,3,4,0) 62%, var(--hill) 86%),
      radial-gradient(circle at 550px 420px,
        var(--moon-core) 0,
        var(--moon-mid) 360px,
        var(--moon-rim) 405px,
        var(--glow) 500px,
        var(--night) 700px);
  }
  .headline {
    position: absolute;
    top: 290px;
    left: 0;
    width: 100%;
  }
  .headline__intro {
    font-family: "Playfair Display", Georgia, serif;
    font-weight: 500;
    font-size: 40px;
    letter-spacing: 3px;
    color: var(--ink-dark);
  }
  .headline__title {
    margin-top: 12px;
    font-family: "Playfair Display", Georgia, serif;
    font-weight: 600;
    font-size: 96px;
    line-height: 1.05;
    color: var(--crimson);
  }
  .details {
    position: absolute;
    top: 1165px;
    left: 0;
    width: 100%;
  }
  .details__date {
    font-size: 40px;
    font-weight: 500;
    letter-spacing: 4px;
  }
  .details__at {
    margin-top: 6px;
    font-size: 30px;
    font-weight: 500;
    letter-spacing: 3px;
  }
  .venue {
    margin: 14px auto 0;
    width: 780px;
    padding: 14px 0 16px;
    border: 3px solid var(--line-light);
    border-radius: 60px;
  }
  .venue__name {
    font-family: "Playfair Display", Georgia, serif;
    font-size: 42px;
    font-weight: 500;
    letter-spacing: 2px;
  }
  .venue__address {
    margin-top: 4px;
    font-size: 26px;
    font-weight: 600;
    letter-spacing: 1px;
  }
  .details__costumes {
    margin-top: 34px;
    font-size: 28px;
    font-weight: 500;
    letter-spacing: 4px;
  }
  .details__adults {
    margin-top: 14px;
    font-size: 28px;
    font-weight: 600;
    letter-spacing: 3px;
    color: var(--crimson);
  }
</style>
</head>
<body>
  <main class="invite">
    <div class="moonlit-scene" role="img" aria-label="Illustration of a large glowing pink full moon over a dark hill with a castle silhouette and flying bats"></div>

    <header class="headline">
      <p class="headline__intro">YOU ARE INVITED TO</p>
      <h1 class="headline__title">THE GARDEN<br>OF EDEN</h1>
    </header>

    <section class="details">
      <p class="details__date">SAT OCT 26 7:00PM</p>
      <p class="details__at">AT</p>
      <div class="venue">
        <p class="venue__name">DINAH &amp; TOBIAS'S HOME</p>
        <p class="venue__address">612 NORTH BIRCH RD 7B</p>
      </div>
      <p class="details__costumes">COSTUMES HIGHLY ENCOURAGED</p>
      <p class="details__adults">ADULTS ONLY PLEASE</p>
    </section>
  </main>
</body>
</html>
```